Church Lanterns Over Millbrook Gospel Booklet Design

We need a booklet designed that we will be printing to hand out in our community. Wording for each page will be provided and we need graphic design to produce the layouts in a format ready for print. Booklet will be 4.75" x 4.75" square and a total of 12 pages: 1 cover page front, 1 cover page back, 10 inside pages some of which will be full spread across 2 pages.

Target Market(s)

English speaking Westerners

Industry/Entity Type

Religious

Font styles to use
Serif

Colors
ffffff
85abd2
0292cd
33b8a4
5c5c5c

Requirements
Must have
• Minimalist design with clean look described in attached document
Nice to have
• Aesthetically pleasing graphics, crisp fonts, excellent turn around times
Should not have
• Effeminate design, busy look with too much graphic and text

```html
<!DOCTYPE html>
<html lang="en">
<head>
<meta charset="utf-8">
<title>Lanterns Over Millbrook – Booklet Pages</title>
<link href="https://fonts.googleapis.com/css2?family=Lato:wght@400;700&family=Oswald:wght@500&display=swap" rel="stylesheet">
<style>
:root{
  --board:#3b3b3d;
  --paper:#ffffff;
  --ink-blue:#1b8fcf;
  --ink-gray:#4a4a4a;
  --ink-dark:#333333;
  --badge:#55585b;
}
*{margin:0;padding:0;box-sizing:border-box}
html,body{width:1200px;height:926px;overflow:hidden;background:var(--board)}
.board{position:relative;width:1200px;height:926px;background:var(--board);font-family:'Lato',sans-serif}
.page{position:absolute;width:266px;height:266px;background:var(--paper);overflow:hidden}
.photo{position:absolute;left:0;top:0;width:266px;height:266px;z-index:0}
.hills{position:absolute;left:0;bottom:0;width:266px;height:104px;display:block;z-index:1}
.hills.cover{height:64px}
.hills.tall{height:102px}
.copy,.quote,.ref,.list,.overlay-copy,.badge,.cover-title,.cover-frame{z-index:2}
.badge{position:absolute;bottom:0;width:26px;height:30px}
.badge svg{position:absolute;inset:0;width:100%;height:100%}
.badge span{position:relative;display:block;text-align:center;color:#fff;font-size:17px;line-height:34px}
.badge.left{left:21px}.badge.right{right:21px}
.badge.wide{width:29px}
.copy{position:absolute;left:18px;right:18px;color:var(--ink-blue);text-align:center;font-size:9.2px;line-height:11.2px}
.quote{position:absolute;left:10px;right:10px;text-align:center;color:var(--ink-blue);font-size:18px;line-height:22px}
.ref{position:absolute;left:0;right:0;text-align:center;color:var(--ink-blue);font-size:10.4px;line-height:12px}
.list{position:absolute;left:29px;right:33px;top:80px;color:var(--ink-blue);font-size:7.2px;line-height:9.3px;padding-left:9px}
.cover-title{position:absolute;right:34px;top:36px;font-family:'Oswald',sans-serif;font-weight:500;color:var(--ink-gray);font-size:26px;line-height:29px;text-align:right;text-transform:uppercase;letter-spacing:.3px}
.cover-frame{position:absolute;top:19px;right:20px;width:141px;height:158px;border-top:2px solid var(--ink-gray);border-right:2px solid var(--ink-gray)}
.overlay-copy{position:absolute;left:17px;right:19px;top:24px;color:var(--ink-dark);font-size:9.2px;line-height:11.2px}
</style>
</head>
<body>
<svg width="0" height="0" style="position:absolute">
  <defs>
    <symbol id="ridge-pale" viewBox="0 0 266 104" preserveAspectRatio="none">
      <path fill="#cde8e7" d="M0 16 C28 6 50 16 80 9 S130 0 160 8 S210 2 240 11 S258 8 266 8 V104 H0Z"/>
      <path fill="#b9dcdb" d="M0 40 C25 32 45 38 70 31 S120 39 150 33 S200 25 230 35 S255 31 266 29 V104 H0Z"/>
      <path fill="#a5c5c7" d="M0 60 C30 54 55 58 85 50 S140 58 170 52 S220 48 266 54 V104 H0Z"/>
    </symbol>
    <symbol id="ridge-deep" viewBox="0 0 266 104" preserveAspectRatio="none">
      <path fill="#5cbcb8" d="M0 18 C30 8 55 16 84 8 S140 2 170 12 S220 4 266 10 V104 H0Z"/>
      <path fill="#2f939a" d="M0 42 C32 34 60 42 90 34 S150 30 182 40 S236 34 266 38 V104 H0Z"/>
      <path fill="#1c6e78" d="M0 66 C30 58 60 64 92 56 S156 54 188 62 S240 58 266 62 V104 H0Z"/>
    </symbol>
    <symbol id="badge-shape" viewBox="0 0 26 30" preserveAspectRatio="none">
      <path fill="#55585b" d="M0 30 L0 9 Q0 6 3 4.5 L11 0.6 Q13 -0.3 15 0.6 L23 4.5 Q26 6 26 9 L26 30Z"/>
    </symbol>
  </defs>
</svg>

<main class="board">

  <!-- Cover -->
  <section class="page" style="left:55px;top:55px">
    <div class="photo" role="img" aria-label="Photo of hands folded in prayer against a bright light" style="background:radial-gradient(circle at 36% 66%,#fffbe6 0%,#f3efc9 28%,#ddcfa4 58%,#b9ab8a 100%)"></div>
    <div class="cover-frame"></div>
    <h1 class="cover-title">Lanterns<br>Over<br>Millbrook</h1>
    <svg class="hills cover"><use href="#ridge-deep"/></svg>
  </section>

  <!-- Page 2 -->
  <section class="page" style="left:330px;top:55px">
    <div class="photo" role="img" aria-label="Black and white photo of a small group studying the Bible together" style="background:linear-gradient(160deg,#c9c9c9 0%,#8c8c8c 45%,#5a5a5a 100%)"></div>
    <svg class="hills tall"><use href="#ridge-deep"/></svg>
    <div class="badge right"><svg><use href="#badge-shape"/></svg><span>2</span></div>
  </section>

  <!-- Page 3 -->
  <section class="page" style="left:605px;top:55px">
    <p class="copy" style="top:36px">God willingly created the universe,<br>meaning he envisioned, designed, and made us.</p>
    <p class="quote" style="top:79px;left:30px;right:30px;font-size:19px;line-height:22.5px">“In the beginning God created the heavens and the earth.”</p>
    <svg class="hills"><use href="#ridge-pale"/></svg>
    <div class="badge left"><svg><use href="#badge-shape"/></svg><span>3</span></div>
  </section>

  <!-- Page 4 -->
  <section class="page" style="left:879px;top:55px">
    <p class="copy" style="top:36px;left:29px;text-align:left">This reality establishes some<br>foundational truths for all of us:</p>
    <ol class="list">
      <li>God loves us - he didn't have to create us; we are here because he couldn't imagine life without us.</li>
      <li>God is the proper authority in our lives - if he designed and made us, he rightfully owns us.</li>
      <li>God knows the purpose of our lives - if he designed and made us, he knows why we are here.</li>
      <li>God's truth is the truth we need - if he designed and made us, he knows what it takes for life to go well for us.</li>
    </ol>
    <svg class="hills"><use href="#ridge-pale"/></svg>
    <div class="badge right"><svg><use href="#badge-shape"/></svg><span>4</span></div>
  </section>

  <!-- Page 5 -->
  <section class="page" style="left:55px;top:330px">
    <p class="copy" style="top:38px;left:24px;right:24px">God willingly created the universe, meaning he envisioned, designed, But we, mankind, have all rejected God's authority in our lives. And because he rightfully owns us, our rebellion against God is a grave injustice; an act of treason for which we deserve to be cut off from God forever. and made us.</p>
    <p class="quote" style="top:132px">“For the wages of sin<br>is death...”</p>
    <p class="ref" style="top:184px">(Romans 6:23)</p>
    <svg class="hills"><use href="#ridge-pale"/></svg>
    <div class="badge left"><svg><use href="#badge-shape"/></svg><span>5</span></div>
  </section>

  <!-- Page 6 -->
  <section class="page" style="left:330px;top:330px">
    <div class="photo" role="img" aria-label="Sepia photo of a cross on a hilltop under a glowing sky" style="background:linear-gradient(180deg,#e4e0dc 0%,#c8c1bb 40%,#f1ece6 60%,#8c8480 78%,#6c6663 100%)"></div>
    <p class="overlay-copy">This alienation from God is evident in a myriad of ways including poverty, crime, conflict in our relationships, and our internal struggles. But worse, when we die, we must face the consequences for our rejection of God by spending eternity in hell - a lake of fire created by God as the place where our treason is brought to justice.</p>
    <svg class="hills"><use href="#ridge-pale"/></svg>
    <div class="badge right"><svg><use href="#badge-shape"/></svg><span>6</span></div>
  </section>

  <!-- Page 7 -->
  <section class="page" style="left:605px;top:330px">
    <p class="copy" style="top:36px;left:19px;right:19px">But God does not want you to pay for your own sins. God loves us so much he sent his only son to save us. Jesus Christ died on the cross to serve our sentence for our rebellion against God and rose again on the third day. Since Christ paid our full penalty, we can be completely forgiven and reconciled to God.</p>
    <p class="quote" style="top:114px;font-size:13px;line-height:16px;left:11px;right:11px">“For God so loved the world that he sent his one and only son that whosoever believes in him will not perish but have eternal life.”</p>
    <p class="ref" style="top:188px">(John 3:16)</p>
    <svg class="hills"><use href="#ridge-pale"/></svg>
    <div class="badge left"><svg><use href="#badge-shape"/></svg><span>7</span></div>
  </section>

  <!-- Page 8 -->
  <section class="page" style="left:879px;top:330px">
    <p class="copy" style="top:37px;left:17px;right:17px">First, ask Jesus Christ to save you (Since he is God, he can hear you): Acknowledge that God is the rightful authority of the universe and your life. Apologize to him for your rebellion against God. Ask Jesus Christ to come into your life as your Lord and Savior. This decision will immediately trigger his miracle of salvation in you. God now lives in you!</p>
    <svg class="hills"><use href="#ridge-pale"/></svg>
    <div class="badge right"><svg><use href="#badge-shape"/></svg><span>8</span></div>
  </section>

  <!-- Page 9 -->
  <section class="page" style="left:55px;top:606px">
    <p class="quote" style="top:38px;font-size:13.8px;line-height:16.8px;left:22px;right:22px">“If you confess with your mouth that Jesus is Lord and believe in your heart that God raised him from the dead, you will be saved.”</p>
    <p class="ref" style="top:111px">(Romans 10:9)</p>
    <svg class="hills"><use href="#ridge-pale"/></svg>
    <div class="badge left"><svg><use href="#badge-shape"/></svg><span>9</span></div>
  </section>

  <!-- Page 10 -->
  <section class="page" style="left:330px;top:606px">
    <p class="copy" style="top:37px;left:16px;right:16px">Next, God has given us the Bible and his church as the key tools for us to grow in our understanding of God and our personal relationship with him. So, it is essential you find a local church that believes the Bible is 100% true. Tell one of the pastors you are a brand new Christian and they will help you from there.</p>
    <svg class="hills"><use href="#ridge-pale"/></svg>
    <div class="badge right wide"><svg><use href="#badge-shape"/></svg><span>10</span></div>
  </section>

  <!-- Page 11 -->
  <section class="page" style="left:605px;top:606px">
    <svg class="hills"><use href="#ridge-pale"/></svg>
    <div class="badge left wide"><svg><use href="#badge-shape"/></svg><span>11</span></div>
  </section>

  <!-- Back cover -->
  <section class="page" style="left:879px;top:606px">
    <div class="photo" role="img" aria-label="Sepia photo of praying hands holding a rosary over an open Bible" style="background:radial-gradient(circle at 55% 40%,#d8d2cc 0%,#9a928c 40%,#3e3a38 80%,#2a2726 100%)"></div>
    <svg class="hills"><use href="#ridge-pale"/></svg>
  </section>

</main>
</body>
</html>
```